Tranquilly Balanced Restoration

We want to design a business card that is modern and appealing for an innovative psychedelic telemedicine company that provides at-home ketamine-assisted therapy along with wellness, longevity, and anti-aging medicines. We want to use our deep purple and white plus other colors you can find on our website. We don't have any strict brand guidelines yet so feel free to get creative. We want a very professional, but technology first modern design that will instill trust, peace, calm, but also be attractive to investors in the healthcare and SaaS space.

```html
<!DOCTYPE html>
<html lang="en">
<head>
<meta charset="utf-8">
<title>Tranquilly – Business Card</title>
<link href="https://fonts.googleapis.com/css2?family=Marcellus&display=swap" rel="stylesheet">
<style>
  :root {
    --backdrop: #efe9e1;
    --card-purple: #59408c;
    --card-purple-light: #654c98;
    --ink-white: #ffffff;
    --ink-soft: rgba(255,255,255,0.85);
  }
  * { margin: 0; padding: 0; box-sizing: border-box; }
  html, body { width: 1200px; height: 900px; overflow: hidden; }
  body {
    background: var(--backdrop);
    font-family: "Marcellus", serif;
    color: var(--ink-white);
    display: flex;
    flex-direction: column;
    align-items: center;
    justify-content: center;
    gap: 44px;
  }
  .card {
    width: 620px;
    height: 354px;
    background: linear-gradient(135deg, var(--card-purple) 0%, var(--card-purple-light) 100%);
    border-radius: 3px;
    box-shadow: 0 10px 24px rgba(60, 40, 90, 0.18);
    position: relative;
    overflow: hidden;
  }

  /* Front */
  .card-front {
    display: flex;
    flex-direction: column;
    align-items: center;
    justify-content: center;
  }
  .brand {
    display: flex;
    align-items: center;
    gap: 16px;
  }
  .brand-dot {
    width: 22px; height: 22px;
    border-radius: 50%;
    background: var(--ink-white);
  }
  .brand-name {
    font-size: 62px;
    letter-spacing: 0.5px;
    line-height: 1;
  }
  .front-url {
    margin-top: 26px;
    font-size: 15px;
    letter-spacing: 6px;
    color: var(--ink-soft);
    padding-left: 38px;
  }

  /* Back */
  .card-back { padding: 44px 40px 34px 48px; }
  .card-back .brand-name { font-size: 52px; }
  .card-back .brand-dot { width: 18px; height: 18px; }
  .back-bottom {
    position: absolute;
    left: 48px; right: 36px; bottom: 32px;
    display: flex;
    justify-content: space-between;
    align-items: flex-end;
  }
  .contact-list { list-style: none; display: flex; flex-direction: column; gap: 7px; }
  .contact-item {
    display: flex; align-items: center; gap: 10px;
    font-size: 16px;
  }
  .contact-icon {
    width: 20px; height: 20px;
    border: 1.3px solid var(--ink-white);
    border-radius: 50%;
    display: flex; align-items: center; justify-content: center;
    flex-shrink: 0;
  }
  .contact-icon svg { width: 11px; height: 11px; }
  .address {
    display: flex; align-items: flex-end; gap: 10px;
    text-align: right;
    font-size: 16px;
    line-height: 1.35;
  }
</style>
</head>
<body>

  <section class="card card-front">
    <div class="brand">
      <span class="brand-dot"></span>
      <span class="brand-name">Tranquilly</span>
    </div>
    <p class="front-url">www.tranquillyrestore.com</p>
  </section>

  <section class="card card-back">
    <div class="brand">
      <span class="brand-dot"></span>
      <span class="brand-name">Tranquilly</span>
    </div>

    <div class="back-bottom">
      <ul class="contact-list">
        <li class="contact-item">
          <span class="contact-icon">
            <svg viewBox="0 0 24 24" fill="none" stroke="#fff" stroke-width="2.4" stroke-linecap="round"><path d="M5 3h4l2 5-2.5 1.5a11 11 0 0 0 6 6L16 13l5 2v4a2 2 0 0 1-2 2A16 16 0 0 1 3 5a2 2 0 0 1 2-2z"/></svg>
          </span>+1 833-555-0148
        </li>
        <li class="contact-item">
          <span class="contact-icon">
            <svg viewBox="0 0 24 24" fill="none" stroke="#fff" stroke-width="2.4"><rect x="3" y="5" width="18" height="14" rx="1"/><path d="M3 6l9 7 9-7"/></svg>
          </span>hello@tranquillyrestore.com
        </li>
        <li class="contact-item"><span class="contact-icon"></span>gotranquilly</li>
        <li class="contact-item"><span class="contact-icon"></span>gotranquilly</li>
        <li class="contact-item"><span class="contact-icon"></span>gotranquilly</li>
      </ul>

      <div class="address">
        <p>245 Aspen Row, Suite 900<br>Boulder, CO, United States, Colorado</p>
        <span class="contact-icon">
          <svg viewBox="0 0 24 24" fill="none" stroke="#fff" stroke-width="2.4"><path d="M12 22s7-7 7-12a7 7 0 0 0-14 0c0 5 7 12 7 12z"/><circle cx="12" cy="10" r="2.5"/></svg>
        </span>
      </div>
    </div>
  </section>

</body>
</html>
```